Make a website for Velmoro, a Luxury and Modern Concierge Platform based in the UAE

Concierge Platform that has various luxury and exotic actives available to clients, itinerary planning for a dubai / uae based holiday.
Want the website to appear luxury, modern and easy to understand, with a landing page that can captivate customers, majority will use Mobile but Desktop should look good too. Whatsapp Contact pop-out, and email sign up list. Social Link (Facebook, Instagram, Whatsapp, Whatsapp Broadcast, Twitter/X, etc).
Ability to make it Dark and Light themed.
Second page Page that has a list of activities on a drop down/ list, as follows:
Flights
Car Rental
Luxury Car Rental
Chauffer
Yachts/ Boats
Jet Ski / Watersports
Buggies/ ATV
Dining
Tickets/Events
Apartments/ Hotels
Personal Shopping.
Link to competitors, who's websites appear basic and could be 100% improved, for examples:
- https://www.hushedgetaways.example/
- https://www.tavix.example/
- https://www.dubai-latch.example/
- https://thevorlanhouse.example/dubai.html
- https://www.thegildedattendant.example/concierge-service-dubai/
Open to logo designs, we own Velmoro.com.
Colours:
Luxury Style, Black and Gold is often used, but maybe over-used?
A modern colour palette White, Light Blue, Light Grey, but we aren't experts at this, so this isn't by any means strict criteria, let the creative mind run free.
Thank you

```html
<!DOCTYPE html>
<html lang="en">
<head>
<meta charset="utf-8">
<title>Velmoro — Dubai's Finest Concierge</title>
<link rel="stylesheet" href="https://fonts.googleapis.com/css2?family=Outfit:wght@500;600;700&family=Lato:wght@400;700&display=swap">
<style>
:root{
  --teal:#0e9a9a;
  --ink:#111;
  --muted:#444;
  --white:#fff;
  --stage:#8e8e8e;
  --footer:#000;
  --head:'Outfit',sans-serif;
  --body:'Lato',sans-serif;
}
*{box-sizing:border-box;margin:0;padding:0}
html,body{width:1200px;height:2602px;overflow:hidden}
body{background:var(--stage);font-family:var(--body);color:var(--ink);position:relative}
.page{position:absolute;left:99px;top:89px;width:1002px;height:2424px;background:var(--white);overflow:hidden;box-shadow:0 12px 30px rgba(0,0,0,.35)}
.btn{position:absolute;display:flex;align-items:center;justify-content:center;font-family:var(--head);font-weight:600;font-size:9.5px;letter-spacing:.3px;text-transform:uppercase;color:#fff;background:var(--teal);text-decoration:none}
.photo{position:absolute}

/* hero */
.hero{position:absolute;left:0;top:0;width:1002px;height:451px;
  background:
    radial-gradient(ellipse 260px 200px at 560px 150px,rgba(214,178,120,.75) 0%,rgba(214,178,120,0) 100%),
    radial-gradient(ellipse 220px 260px at 860px 120px,rgba(190,200,210,.55) 0%,rgba(190,200,210,0) 100%),
    radial-gradient(ellipse 90px 180px at 670px 360px,rgba(40,32,28,.85) 0%,rgba(40,32,28,0) 100%),
    linear-gradient(180deg,rgba(0,0,0,0) 70%,rgba(30,40,30,.55) 100%),
    linear-gradient(90deg,#161a22 0%,#262830 30%,#4e4739 55%,#7b6a50 75%,#5d5f66 100%)}
.hero-shade{position:absolute;inset:0;background:linear-gradient(90deg,rgba(15,18,25,.7) 0%,rgba(15,18,25,.3) 45%,rgba(0,0,0,0) 70%)}
.logo{position:absolute;left:162px;top:17px;font-family:var(--head);font-weight:600;font-size:22px;letter-spacing:4px;color:var(--teal)}
.nav{position:absolute;top:23px;left:355px}
.nav a{position:absolute;font-size:9px;color:#fff;text-decoration:none;white-space:nowrap}
.nav a.active{color:var(--teal)}
.hero h1{position:absolute;left:162px;top:140px;font-family:var(--head);font-weight:600;font-size:30px;line-height:36.5px;color:#fff}
.hero h1 em{font-style:normal;color:var(--teal)}
.hero-sub{position:absolute;left:162px;top:263px;font-size:8.5px;color:#fff}
.btn-outline{background:transparent;border:1.5px solid #fff}
.counter{position:absolute;left:752px;top:396px;font-family:var(--head);font-weight:700;font-size:40px;color:#fff}
.counter small{font-size:22px}

/* why */
.section-title{position:absolute;left:0;width:1002px;text-align:center;font-family:var(--head);font-weight:700;font-size:23px}
.section-title em{font-style:normal;color:var(--teal)}
.tagline{position:absolute;left:0;width:1002px;top:545px;text-align:center;font-size:8.5px;color:var(--muted)}
.timeline{position:absolute;left:166px;top:666px;width:669px;border-top:1px dashed #777}
.dot{position:absolute;width:8px;height:8px;border-radius:50%;background:var(--teal);top:662px}
.why-card{position:absolute;top:581px;width:120px;height:172px;background:#fff;box-shadow:0 6px 20px rgba(0,0,0,.1);text-align:center}
.why-card svg.icon{position:absolute;left:39px;top:25px}
.why-card .node{position:absolute;left:54px;top:98px;width:12px;height:12px;border:1px dashed #777;border-radius:50%;background:#fff}
.why-card .stem{position:absolute;left:60px;top:85px;height:13px;border-left:1px dashed #777}
.why-card h3{position:absolute;top:127px;left:0;width:120px;font-family:var(--head);font-weight:600;font-size:12px;line-height:15px}

/* about */
.about-title{position:absolute;left:525px;top:840px;font-family:var(--head);font-weight:700;font-size:24px}
.about-text{position:absolute;left:525px;top:879px;width:314px;font-size:8.3px;line-height:16px;color:var(--muted)}

/* featured */
.featured{position:absolute;left:0;top:1069px;width:1002px;height:353px;
  background:
    radial-gradient(ellipse 160px 200px at 620px 120px,rgba(120,90,60,.55) 0%,rgba(120,90,60,0) 100%),
    radial-gradient(ellipse 140px 220px at 880px 180px,rgba(60,70,80,.6) 0%,rgba(60,70,80,0) 100%),
    linear-gradient(90deg,#2a1e18 0%,#3d2c22 45%,#2d2520 70%,#1f2a30 100%)}
.featured-shade{position:absolute;inset:0;background:rgba(10,8,6,.45)}
.featured h2{position:absolute;left:162px;top:93px;font-family:var(--head);font-weight:600;font-size:23px;color:#fff}
.svc{position:absolute;height:91px;display:flex;align-items:center;gap:14px;color:#fff;font-family:var(--head);font-weight:600;font-size:10px;line-height:12px}
.svc.hl{background:var(--teal);display:block;padding:20px 15px 0}
.svc.hl p{font-family:var(--body);font-weight:400;font-size:8.5px;line-height:12px;margin-top:6px}
.hl-badge{position:absolute;width:42px;height:42px;background:#fff;display:flex;align-items:center;justify-content:center}
.vline{position:absolute;border-left:1px solid rgba(255,255,255,.25)}
.hline{position:absolute;border-top:1px solid rgba(255,255,255,.25)}

/* functionality */
.func-card{position:absolute;top:1515px;width:218px;height:244px;color:#fff}
.func-card .cap{position:absolute;left:18px;top:182px;width:190px}
.func-card h4{font-family:var(--head);font-weight:600;font-size:10px}
.func-card p{font-size:8.5px;line-height:14px;margin-top:4px}
.func-card .arrow{position:absolute;right:19px;bottom:-14px;width:25px;height:25px;background:var(--teal);display:flex;align-items:center;justify-content:center}
.view-all{position:absolute;left:0;width:1002px;top:1790px;text-align:center;font-family:var(--head);font-weight:600;font-size:9px}
.view-all a{color:var(--ink);text-decoration:underline}

/* testimonials */
.testi-left{position:absolute;left:0;top:1848px;width:501px;height:319px;
  background:
    radial-gradient(ellipse 140px 120px at 160px 250px,rgba(150,160,160,.25) 0%,rgba(150,160,160,0) 100%),
    linear-gradient(120deg,#ebe9e7 0%,#dedad6 60%,#e4e2df 100%)}
.testi-left h2{position:absolute;left:162px;top:62px;font-family:var(--head);font-weight:700;font-size:23px}
.stars{position:absolute;left:162px;top:98px;display:flex;gap:3px}
.testi-left p.quote{position:absolute;left:162px;top:120px;width:290px;font-size:8.5px;line-height:16px;color:var(--muted)}
.avatar{position:absolute;left:162px;top:187px;width:36px;height:36px;border-radius:50%;background:linear-gradient(135deg,#d34a4a,#7a2a2a)}
.who{position:absolute;left:211px;top:194px;font-size:9px;line-height:11px}
.who b{font-family:var(--head);font-weight:600}
.testi-nav{position:absolute;left:162px;top:241px}

/* footer */
.footer{position:absolute;left:0;top:2167px;width:1002px;height:257px;background:var(--footer);color:#fff}
.footer h5{position:absolute;top:56px;font-family:var(--head);font-weight:600;font-size:11px}
.footer ul{position:absolute;top:86px;list-style:none;font-size:8.5px;line-height:17.6px}
.contact{position:absolute;left:462px;top:86px;font-size:8.5px;line-height:10px}
.contact b{font-family:var(--head);font-weight:600;display:block}
.contact div{margin-bottom:12px}
.news-label{position:absolute;left:659px;top:86px;font-size:8.5px}
.news-input{position:absolute;left:659px;top:102px;width:181px;height:32px;background:#2b2b2b;display:flex;align-items:center;justify-content:space-between;padding:0 10px 0 12px;font-size:8.5px;color:#aaa}
.foot-line{position:absolute;left:162px;top:218px;width:678px;border-top:1px solid #333}
.to-top{position:absolute;left:849px;top:203px;width:31px;height:31px;background:var(--teal);display:flex;align-items:center;justify-content:center}
.copy{position:absolute;left:0;top:233px;width:1002px;text-align:center;font-size:8.5px}
</style>
</head>
<body>
<div class="page">

  <section class="hero" role="img" aria-label="Businessman in a suit gazing over the Dubai skyline at sunset from a high-rise window">
    <div class="hero-shade"></div>
    <div class="logo">VELMORO</div>
    <nav class="nav">
      <a class="active" style="left:0">Home</a>
      <a style="left:48px">Services</a>
      <a style="left:107px">Lifestyle</a>
      <a style="left:167px">Experiences</a>
      <a style="left:242px">Corporate</a>
      <a style="left:308px">Membership</a>
    </nav>
    <a class="btn" style="left:736px;top:13px;width:103px;height:31px">Get Started</a>
    <h1>“Dubai’s Finest<br><em>Concierge</em> at Your<br>Fingertips”</h1>
    <p class="hero-sub">Exclusive lifestyle services tailored to your every desire.”</p>
    <a class="btn" style="left:162px;top:290px;width:111px;height:32px">Explore Services</a>
    <a class="btn btn-outline" style="left:283px;top:290px;width:87px;height:32px">Contact Us</a>
    <div class="counter">01/<small>03</small></div>
  </section>

  <h2 class="section-title" style="top:508px">Why Choose <em>Velmoro?</em></h2>
  <p class="tagline">Trust &amp; Luxury</p>
  <div class="timeline"></div>
  <div class="dot" style="left:162px"></div>
  <div class="dot" style="left:831px"></div>

  <div class="why-card" style="left:212px">
    <svg class="icon" width="42" height="40" viewBox="0 0 42 40" fill="none" stroke="#0e9a9a" stroke-width="1.6"><rect x="5" y="3" width="32" height="24" rx="2"/><path d="M1 31h40l-3 4H4z"/><circle cx="21" cy="10" r="4"/><path d="M19 10l1.5 1.5L23 9"/><rect x="11" y="16" width="20" height="6" rx="1"/><circle cx="15" cy="19" r=".8"/><circle cx="21" cy="19" r=".8"/><circle cx="27" cy="19" r=".8"/></svg>
    <div class="stem"></div><div class="node"></div>
    <h3>Exclusive<br>Access</h3>
  </div>
  <div class="why-card" style="left:365px">
    <svg class="icon" width="42" height="40" viewBox="0 0 42 40" fill="none" stroke="#0e9a9a" stroke-width="1.6"><rect x="3" y="2" width="36" height="36" rx="3"/><path d="M3 8h36"/><circle cx="14" cy="25" r="5"/><path d="M8 34c1-4 11-4 12 0"/><path d="M29 13a4 4 0 0 1 4 4c0 3-4 7-4 7s-4-4-4-7a4 4 0 0 1 4-4z"/><path d="M20 30c4 0 9-1 9-5" stroke-dasharray="2 2"/></svg>
    <div class="stem"></div><div class="node"></div>
    <h3>Personalized<br>Itineraries</h3>
  </div>
  <div class="why-card" style="left:517px">
    <svg class="icon" width="42" height="40" viewBox="0 0 42 40" fill="none" stroke="#0e9a9a" stroke-width="1.6"><rect x="12" y="2" width="14" height="6"/><path d="M12 8v6a7 7 0 0 0 14 0V8"/><path d="M8 38v-9a6 6 0 0 1 6-6h10a6 6 0 0 1 6 6v9"/><rect x="27" y="20" width="12" height="16" rx="2"/><path d="M30 20v-3h6v3"/><rect x="3" y="30" width="10" height="8"/></svg>
    <div class="stem"></div><div class="node"></div>
    <h3>24/7<br>Concierge</h3>
  </div>
  <div class="why-card" style="left:670px">
    <svg class="icon" width="42" height="40" viewBox="0 0 42 40" fill="none" stroke="#0e9a9a" stroke-width="1.6"><circle cx="13" cy="12" r="6"/><path d="M6 8h14"/><path d="M2 38v-8a7 7 0 0 1 7-7h8a7 7 0 0 1 7 7"/><rect x="25" y="2" width="14" height="12"/><path d="M32 5l1 2 2 .3-1.5 1.4.4 2-1.9-1-1.9 1 .4-2L29 7.3l2-.3z"/><circle cx="32" cy="29" r="8"/><path d="M28 29h8M32 25l3 4-3 4"/></svg>
    <div class="stem"></div><div class="node"></div>
    <h3>Luxury Travel<br>Experts</h3>
  </div>

  <section class="featured">
    <div class="photo" role="img" aria-label="Hotel lobby with concierge staff in waistcoats and bow ties" style="inset:0"></div>
    <div class="featured-shade"></div>
    <h2>Featured Services</h2>
    <a class="btn" style="left:750px;top:89px;width:90px;height:32px">Read More</a>

    <div class="vline" style="left:331px;top:139px;height:182px"></div>
    <div class="vline" style="left:671px;top:222px;height:99px"></div>
    <div class="vline" style="left:501px;top:222px;height:99px"></div>
    <div class="hline" style="left:149px;top:222px;width:704px"></div>

    <div class="svc" style="left:192px;top:130px">
      <svg width="38" height="38" viewBox="0 0 38 38" fill="none" stroke="#fff" stroke-width="1.5"><path d="M13 4h12v6H13z"/><path d="M8 20l3-9h16l3 9"/><rect x="4" y="20" width="30" height="9" rx="2"/><circle cx="10" cy="24.5" r="2"/><circle cx="28" cy="24.5" r="2"/><path d="M7 29v4h5v-4M26 29v4h5v-4"/></svg>
      <span>Luxury Car<br>Rentals</span>
    </div>
    <div class="svc" style="left:345px;top:130px">
      <svg width="38" height="38" viewBox="0 0 38 38" fill="none" stroke="#fff" stroke-width="1.5"><circle cx="8" cy="8" r="3"/><path d="M8 1v2M8 13v2M1 8h2M13 8h2"/><path d="M26 8c2-2 4-2 6 0"/><path d="M3 27h32l-4 6H7z"/><path d="M9 27v-5h18v5M14 22v-5h10v5"/><path d="M2 36c3-2 5-2 8 0s5 2 8 0 5-2 8 0 5 2 8 0"/></svg>
      <span>Private Yachts</span>
    </div>
    <div class="svc hl" style="left:501px;top:139px;width:170px;height:91px">
      <span>Exclusive Dining</span>
      <p>Lorem ipsum dolor sit amet, consectetuer adipiscing elit, sed diam nonummy.</p>
    </div>
    <div class="hl-badge" style="left:516px;top:118px">
      <svg width="32" height="30" viewBox="0 0 38 36" fill="none" stroke="#0e9a9a" stroke-width="1.5"><path d="M4 5l1 2 2 .3-1.5 1.4.4 2L4 9.7 2 10.7l.4-2L1 7.3 3 7z"/><path d="M13 3l1 2 2 .3-1.5 1.4.4 2L13 7.7 11 8.7l.4-2L10 5.3 12 5z"/><path d="M25 3l1 2 2 .3-1.5 1.4.4 2L25 7.7 23 8.7l.4-2L22 5.3 24 5z"/><path d="M34 5l1 2 2 .3-1.5 1.4.4 2L34 9.7 32 10.7l.4-2L31 7.3 33 7z"/><path d="M6 24a13 13 0 0 1 26 0"/><path d="M2 24h34v4H2z"/><path d="M6 28v6h26v-6M11 28v6M16 28v6M22 28v6M27 28v6"/></svg>
    </div>
    <div class="svc" style="left:701px;top:130px">
      <svg width="38" height="38" viewBox="0 0 38 38" fill="none" stroke="#fff" stroke-width="1.5"><rect x="4" y="3" width="22" height="32" rx="1"/><path d="M9 10h12M9 16h12M9 22h8M9 28h8"/><path d="M20 30l14-14 3 3-14 14-4 1z"/></svg>
      <span>Jet Charter</span>
    </div>

    <div class="svc" style="left:192px;top:222px">
      <svg width="38" height="38" viewBox="0 0 38 38" fill="none" stroke="#fff" stroke-width="1.5"><path d="M13 4h12v6H13z"/><path d="M8 20l3-9h16l3 9"/><rect x="4" y="20" width="30" height="9" rx="2"/><circle cx="10" cy="24.5" r="2"/><circle cx="28" cy="24.5" r="2"/><path d="M7 29v4h5v-4M26 29v4h5v-4"/></svg>
      <span>Luxury Car<br>Rentals</span>
    </div>
    <div class="svc" style="left:345px;top:222px">
      <svg width="38" height="38" viewBox="0 0 38 38" fill="none" stroke="#fff" stroke-width="1.5"><circle cx="8" cy="8" r="3"/><path d="M8 1v2M8 13v2M1 8h2M13 8h2"/><path d="M26 8c2-2 4-2 6 0"/><path d="M3 27h32l-4 6H7z"/><path d="M9 27v-5h18v5M14 22v-5h10v5"/><path d="M2 36c3-2 5-2 8 0s5 2 8 0 5-2 8 0 5 2 8 0"/></svg>
      <span>Private Yachts</span>
    </div>
    <div class="svc" style="left:514px;top:222px">
      <svg width="38" height="38" viewBox="0 0 38 36" fill="none" stroke="#fff" stroke-width="1.5"><path d="M4 5l1 2 2 .3-1.5 1.4.4 2L4 9.7 2 10.7l.4-2L1 7.3 3 7z"/><path d="M13 3l1 2 2 .3-1.5 1.4.4 2L13 7.7 11 8.7l.4-2L10 5.3 12 5z"/><path d="M25 3l1 2 2 .3-1.5 1.4.4 2L25 7.7 23 8.7l.4-2L22 5.3 24 5z"/><path d="M34 5l1 2 2 .3-1.5 1.4.4 2L34 9.7 32 10.7l.4-2L31 7.3 33 7z"/><path d="M6 24a13 13 0 0 1 26 0"/><path d="M2 24h34v4H2z"/><path d="M6 28v6h26v-6M11 28v6M16 28v6M22 28v6M27 28v6"/></svg>
      <span>Exclusive Dining</span>
    </div>
    <div class="svc" style="left:701px;top:222px">
      <svg width="38" height="38" viewBox="0 0 38 38" fill="none" stroke="#fff" stroke-width="1.5"><rect x="4" y="3" width="22" height="32" rx="1"/><path d="M9 10h12M9 16h12M9 22h8M9 28h8"/><path d="M20 30l14-14 3 3-14 14-4 1z"/></svg>
      <span>Jet Charter</span>
    </div>
  </section>

  <div class="photo" role="img" aria-label="Smiling hotel concierge in a bow tie and waistcoat assisting a guest at the front desk" style="left:162px;top:813px;width:315px;height:319px;background:
    radial-gradient(ellipse 110px 80px at 150px 110px,rgba(235,200,175,.8) 0%,rgba(235,200,175,0) 100%),
    radial-gradient(ellipse 120px 100px at 80px 250px,rgba(245,242,238,.9) 0%,rgba(245,242,238,0) 100%),
    radial-gradient(ellipse 70px 120px at 150px 230px,rgba(20,18,18,.85) 0%,rgba(20,18,18,0) 100%),
    linear-gradient(135deg,#4a2414 0%,#7a4528 40%,#9a6a48 60%,#3a2a22 100%)"></div>
  <h2 class="about-title">About Velmoro</h2>
  <p class="about-text">Velmoro is a premier concierge service in the UAE, specializing in exclusive, tailor-made luxury experiences. From private yacht charters to VIP dining, we curate the finest services for elite travelers, ensuring every moment is seamless and extraordinary.</p>
  <a class="btn" style="left:525px;top:958px;width:90px;height:32px">Read More</a>

  <h2 class="section-title" style="top:1465px">Functionality</h2>

  <div class="func-card" style="left:162px">
    <div class="photo" role="img" aria-label="Woman in a camel coat holding a phone and passport in an airport terminal" style="inset:0;background:
      radial-gradient(ellipse 70px 110px at 110px 150px,rgba(200,160,110,.9) 0%,rgba(200,160,110,0) 100%),
      linear-gradient(180deg,#a8b0b4 0%,#8e8a84 40%,#5a4f44 100%)"></div>
    <div class="photo" style="inset:0;background:linear-gradient(180deg,rgba(0,0,0,0) 55%,rgba(0,0,0,.6) 100%)"></div>
    <div class="cap"><h4>Exclusive Access</h4><p>Lorem ipsum dolor sit amet, consectetuer adipiscing elit.</p></div>
    <div class="arrow"><svg width="10" height="10" viewBox="0 0 10 10" fill="none" stroke="#fff" stroke-width="1.6"><path d="M3 1l4 4-4 4"/></svg></div>
  </div>
  <div class="func-card" style="left:392px">
    <div class="photo" role="img" aria-label="Hands filling in a travel form on a clipboard beside a passport" style="inset:0;background:
      radial-gradient(ellipse 80px 60px at 90px 80px,rgba(250,250,250,.9) 0%,rgba(250,250,250,0) 100%),
      radial-gradient(ellipse 60px 50px at 150px 60px,rgba(230,160,70,.5) 0%,rgba(230,160,70,0) 100%),
      linear-gradient(160deg,#d8d8d6 0%,#b8b4ae 50%,#3c4256 100%)"></div>
    <div class="photo" style="inset:0;background:linear-gradient(180deg,rgba(0,0,0,0) 55%,rgba(0,0,0,.6) 100%)"></div>
    <div class="cap"><h4>Personalized Itineraries</h4><p>Lorem ipsum dolor sit amet, consectetuer adipiscing elit.</p></div>
    <div class="arrow"><svg width="10" height="10" viewBox="0 0 10 10" fill="none" stroke="#fff" stroke-width="1.6"><path d="M3 1l4 4-4 4"/></svg></div>
  </div>
  <div class="func-card" style="left:622px">
    <div class="photo" role="img" aria-label="Hand pressing a silver reception bell on a dark desk" style="inset:0;background:
      radial-gradient(ellipse 40px 30px at 130px 130px,rgba(210,210,210,.8) 0%,rgba(210,210,210,0) 100%),
      radial-gradient(ellipse 50px 30px at 60px 110px,rgba(190,130,100,.6) 0%,rgba(190,130,100,0) 100%),
      linear-gradient(160deg,#1e1d1c 0%,#3a3634 50%,#141313 100%)"></div>
    <div class="cap"><h4>24/7 Concierge</h4><p>Lorem ipsum dolor sit amet, consectetuer adipiscing elit.</p></div>
    <div class="arrow"><svg width="10" height="10" viewBox="0 0 10 10" fill="none" stroke="#fff" stroke-width="1.6"><path d="M3 1l4 4-4 4"/></svg></div>
  </div>
  <p class="view-all"><a>VIEW ALL PROJECT</a></p>

  <section class="testi-left" role="img" aria-label="Faded hotel lobby scene behind the testimonial">
    <h2>Testimonials</h2>
    <div class="stars">
      <svg width="13" height="13" viewBox="0 0 24 24" fill="#f5c518"><path d="M12 2l3 7 7 .6-5.3 4.6 1.6 7L12 17.5 5.7 21.2l1.6-7L2 9.6 9 9z"/></svg>
      <svg width="13" height="13" viewBox="0 0 24 24" fill="#f5c518"><path d="M12 2l3 7 7 .6-5.3 4.6 1.6 7L12 17.5 5.7 21.2l1.6-7L2 9.6 9 9z"/></svg>
      <svg width="13" height="13" viewBox="0 0 24 24" fill="#f5c518"><path d="M12 2l3 7 7 .6-5.3 4.6 1.6 7L12 17.5 5.7 21.2l1.6-7L2 9.6 9 9z"/></svg>
      <svg width="13" height="13" viewBox="0 0 24 24" fill="#f5c518"><path d="M12 2l3 7 7 .6-5.3 4.6 1.6 7L12 17.5 5.7 21.2l1.6-7L2 9.6 9 9z"/></svg>
      <svg width="13" height="13" viewBox="0 0 24 24" fill="#f5c518"><path d="M12 2l3 7 7 .6-5.3 4.6 1.6 7L12 17.5 5.7 21.2l1.6-7L2 9.6 9 9z"/></svg>
    </div>
    <p class="quote">Lorem ipsum dolor sit amet, consectetuer adipiscing elit, sed diam nonummy nibh euismod tincidunt ut laoreet dolore magna aliquam erat volutpat.</p>
    <div class="avatar" role="img" aria-label="Reviewer portrait"></div>
    <div class="who"><b>Marcus T.</b><br>Project Manger</div>
    <svg class="testi-nav" width="46" height="12" viewBox="0 0 46 12" fill="none" stroke-width="1.3"><path d="M11 6H1M5 2L1 6l4 4" stroke="#333"/><path d="M24 6h20M40 2l4 4-4 4" stroke="#0e9a9a"/></svg>
  </section>
  <div class="photo" role="img" aria-label="Smiling man in a grey suit handing over a passport in a bright hotel lobby" style="left:501px;top:1848px;width:501px;height:319px;background:
    radial-gradient(ellipse 110px 150px at 260px 190px,rgba(150,155,165,.9) 0%,rgba(150,155,165,0) 100%),
    radial-gradient(ellipse 160px 120px at 120px 60px,rgba(200,175,130,.8) 0%,rgba(200,175,130,0) 100%),
    linear-gradient(120deg,#5e4c38 0%,#9a8262 40%,#6c7282 70%,#324474 100%)"></div>

  <footer class="footer">
    <h5 style="left:162px">Why Choose Us</h5>
    <ul style="left:162px"><li>Home</li><li>About Us</li><li>Services</li><li>Project</li><li>Testimonials</li></ul>
    <h5 style="left:316px">Information</h5>
    <ul style="left:316px"><li>Privacy Policy</li><li>Disclaimer</li><li>Terms &amp; Candition</li><li>Site Map</li></ul>
    <h5 style="left:462px">Contact Us</h5>
    <div class="contact">
      <div><b>PHONE</b>(555)014-2287</div>
      <div><b>EMAIL</b>hello@velmoro.example</div>
      <div><b>ADDRESS</b>18 Marina Crest Rd, Suite 210<br>Dubai Marina, UAE</div>
    </div>
    <h5 style="left:659px">Newsletter</h5>
    <p class="news-label">Subscribe to our newsletter</p>
    <div class="news-input"><span>Enter email address</span>
      <svg width="12" height="12" viewBox="0 0 24 24" fill="#fff"><path d="M22 2L2 10l8 3 3 8z"/></svg>
    </div>
    <div class="foot-line"></div>
    <div class="to-top"><svg width="8" height="8" viewBox="0 0 10 10" fill="none" stroke="#fff" stroke-width="1.5"><path d="M1 7l4-4 4 4"/></svg></div>
    <p class="copy">Copyright © 2024 Velmoro, LLC All rights reserved | Privacy and cookie policy Terms | Privacy | Cookies</p>
  </footer>

</div>
</body>
</html>
```